Doctor to Patient Management Website

I need a design for a health management website that connects doctors to patients. The website will consist of: A main page mainly describing our goal, services, and initiatives towards (Who we are AKA "About Us", Our services, Contact Us, Quick Links for health tips, Language selection, Find a doctor, search bar, Member Login Section, small glossary section below with links to all entities mentioned prior, Help section (Helpful tips and tutorials, Used to request help from admin, customer service, to resolve issues or get assistance). A profile page with two types:1) Doctor Profile: Doctor Personal info (First, Last, Middle Name, Title), Clinic, Hospital Info, Department, Credentials, Years of Experience, Patients rating, #Patients seen during the current week, #Patients seen in total, Picture, Link to email doctor, Link to print doctor's profile). Tabs for "About Me", "Contact Info", "Ratings & Comments", "Documents" (To be downloaded and uploaded by patient), "Patients (List of Patients alphabetical order by name)", "Calendar" (to see doctor's availability for booking) underneath all links. 2) Patient profile: About me, Personal Info, Height, Weight, Blood Type, Age, DOB, Name, etc..., Message and email link.Picture of patient with menu made of "Personal Data", "Biometrics", "Allergies", "Illnesses", "Medications", "Medical Procedures", "Doctors" treating the patient, "Documents" (To be downloaded and uploaded by patient). Underneath all, other patients he or she is related to (For example: family member, so patient can't connect to other patients who are family members)3) Login section: New Users will have option to register using:First Name (Required), Last Name, Middle (not required), Address (Not required), City (Required), Country (Required), Email (Not required), Phone Number (Required), Choose UserName, Password, Account Type (Doctor or Patient). Once registered, they will log in using UserName, Password, and Account_Type.Curent Users will log in using UserName, Password, and Account_Type and option to retrieve username or password.Pages to include (Login Page - Registration Page - Retrieve Username and Reset Password Page)Please see link below:https://lanternpost-media.example/importance-claiming-vitalrank-quopa-zeltra/Pictures are attached to this project as an inspirationFYI: Dummy text can be used to fill in the business, services, and descriptive information. Feel free to include your own ideas in the layout, design, categories, patterns, and more to and showcase your talent. Design and pictures provided are available as source of ideas.

Target Market(s)

Age: 21+ / Family Oriented / Medical Sector / Metropolitan Area / Educated and non Educated Users

Industry/Entity Type

Health Care

Number of Pages Required

5+ page

Font styles to use
Sans Serif

Colors

Designer to choose colors to be used in the design.

Requirements
Must have
• Thin layer design
• Simple font - No serif
• Clean menu with light but solid colors (No Gradient effect)
Nice to have
• Different color themes (2 or 3) can be combined
• Sample pictures for illustration (either as an ad or to go with the flow of your design)
• Dashboard Feel (Suggested but not required)
Should not have
• Artistic fonts - with Serif
• Dark color themes

```html
<!DOCTYPE html>
<html lang="en">
<head>
<meta charset="utf-8">
<title>Wellvane – Member Login</title>
<link rel="stylesheet" href="https://fonts.googleapis.com/css2?family=Roboto:wght@300;400;500;700&display=swap">
<style>
  :root {
    --hero-yellow: #f6c400;
    --hero-yellow-deep: #eaa800;
    --hero-green: rgba(118, 168, 20, 0.55);
    --hero-green-soft: rgba(150, 170, 30, 0.45);
    --panel-bg: #efefef;
    --ink: #13202f;
    --ink-soft: #3a3a55;
    --field-line: #a9a9a9;
    --login-btn: #3c3c5e;
    --white: #ffffff;
    --muted: #9a9a9a;
    --social-blue: #4f86d1;
  }
  * { margin: 0; padding: 0; box-sizing: border-box; }
  html, body { width: 1200px; height: 752px; overflow: hidden; }
  body { font-family: "Roboto", Arial, sans-serif; background: var(--panel-bg); position: relative; }

  .hero { position: absolute; left: 0; top: 0; width: 770px; height: 752px; overflow: hidden; }
  .hero-photo { position: absolute; inset: 0; background: radial-gradient(ellipse at 55% 45%, #ffd21a 0%, var(--hero-yellow) 45%, var(--hero-yellow-deep) 100%); }
  .hero-shapes { position: absolute; inset: 0; }
  .hero-title { position: absolute; left: 43px; top: 52px; color: var(--white); font-size: 42px; line-height: 42px; font-weight: 400; }
  .hero-title strong { font-weight: 700; }

  .login-panel { position: absolute; left: 770px; top: 0; width: 430px; height: 752px; background: var(--panel-bg); }
  .brand { position: absolute; left: 0; width: 100%; top: 93px; text-align: center; padding-left: 8px; font-size: 33px; font-weight: 500; color: var(--ink); letter-spacing: 0.2px; }

  .field { position: absolute; left: 90px; width: 269px; border-bottom: 1.5px solid var(--field-line); }
  .field-label { display: block; font-size: 8.5px; color: var(--ink-soft); text-transform: uppercase; letter-spacing: 0.2px; }
  .field-value { display: block; font-size: 15px; color: #111; margin-top: 5px; height: 20px; }
  .field-login { top: 199px; }
  .field-password { top: 265px; }
  .dots { display: flex; gap: 8px; padding-top: 8px; padding-left: 4px; }
  .dots span { width: 8px; height: 8px; border-radius: 50%; background: #222; }

  .btn { position: absolute; left: 93px; width: 270px; height: 40px; display: flex; align-items: center; font-size: 12.5px; text-transform: uppercase; }
  .btn-login { top: 356px; background: var(--login-btn); color: var(--white); justify-content: center; font-weight: 500; font-size: 13.5px; box-shadow: 0 2px 3px rgba(0,0,0,0.25); }
  .divider-or { position: absolute; left: 93px; top: 428px; font-size: 8.5px; color: var(--ink-soft); }
  .btn-social { padding-left: 65px; }
  .btn-norvik { top: 458px; background: var(--white); color: var(--muted); }
  .btn-pellaro { top: 526px; background: var(--social-blue); color: var(--white); }
  .btn-mark { position: absolute; left: 22px; top: 9px; }
</style>
</head>
<body>
  <section class="hero">
    <div class="hero-photo" role="img" aria-label="Photo of a young woman cheering with one arm raised while holding a tablet, against a yellow wall"></div>
    <svg class="hero-shapes" width="770" height="752" viewBox="0 0 770 752" aria-hidden="true">
      <circle cx="152" cy="620" r="359" fill="var(--hero-green-soft)"/>
      <circle cx="501" cy="754" r="246" fill="var(--hero-green)"/>
    </svg>
    <h1 class="hero-title">Lead a <strong>Healthy</strong><br>and<br><strong>Happy Life<br>Online.</strong></h1>
  </section>

  <section class="login-panel">
    <div class="brand">Wellvane</div>

    <div class="field field-login">
      <span class="field-label">Login</span>
      <span class="field-value">UserLogin@portal-mail.example</span>
    </div>
    <div class="field field-password">
      <span class="field-label">Password</span>
      <span class="field-value dots"><span></span><span></span><span></span><span></span><span></span><span></span><span></span><span></span></span>
    </div>

    <div class="btn btn-login">Login</div>
    <div class="divider-or">OR</div>

    <div class="btn btn-social btn-norvik">
      <svg class="btn-mark" width="22" height="22" viewBox="0 0 22 22" aria-hidden="true"><circle cx="11" cy="11" r="10" fill="#d0d0d0"/></svg>
      Signup with Norvik
    </div>
    <div class="btn btn-social btn-pellaro">
      <svg class="btn-mark" width="22" height="22" viewBox="0 0 22 22" aria-hidden="true"><rect x="1" y="1" width="20" height="20" rx="2" fill="#ffffff"/></svg>
      Signup with Pellaro
    </div>
  </section>
</body>
</html>
```